Flyer for customer acquisition.

Hello, We are a sportmanagement agency from Germany and we need information flyers for customer acquisition. It should be DinA4 and should have a modern but serious design. I have uploaded a information sheet, where you can find the text and the composition, the flyer should have. I also uploaded Pictures / Images, which you can use. Of course you can use other suitable images. If they are not free, I will buy them later. On the bottom of the flyer there has been the contact information. You will find them in the download section, too. If you have questions, just write me. If I forgot something, I will update the letter :) Thank you very much!
Ich brauche zusätzliche Tage um durchzusehen

```html
<!DOCTYPE html>
<html lang="de">
<head>
<meta charset="utf-8">
<title>Vellmar – Nachwuchsförderung Flyer</title>
<link rel="stylesheet" href="https://fonts.googleapis.com/css2?family=Catamaran:wght@400;600;700;800&display=swap">
<style>
  :root {
    --stage: #5e5e5e;
    --ink: #1b1f24;
    --ink-soft: #262b31;
    --blue: #2a9bd8;
    --white: #ffffff;
    --text: #e9edf1;
    --green-a: #9ed43a;
    --green-b: #d8f06a;
  }
  * { box-sizing: border-box; margin: 0; padding: 0; }
  html, body { width: 1200px; height: 1200px; overflow: hidden; }
  body {
    background: var(--stage);
    font-family: "Catamaran", sans-serif;
    position: relative;
  }
  .flyer {
    position: absolute;
    top: 208px;
    width: 551px;
    height: 784px;
    overflow: hidden;
    background: var(--white);
  }
  .flyer--front { left: 34px; }
  .flyer--back { left: 615px; }
  .flyer__bg { position: absolute; inset: 0; }
  .abs { position: absolute; }

  .brand-name {
    font-weight: 700;
    font-size: 30px;
    letter-spacing: 1px;
    text-align: center;
  }
  .brand-name--dark { color: var(--ink); }
  .brand-name--light { color: var(--white); }

  .title-kicker { left: 15px; top: 108px; color: var(--blue); font-weight: 800; font-size: 30px; }
  .title-main { left: 15px; top: 148px; color: var(--white); font-weight: 800; font-size: 31px; line-height: 38px; }
  .tagline {
    left: 15px; top: 235px; width: 372px; height: 26px;
    background: var(--white); color: var(--blue);
    font-weight: 600; font-size: 17px; line-height: 27px; padding-left: 2px;
  }

  .section__head { color: var(--blue); font-weight: 700; font-size: 16px; line-height: 20px; }
  .section__body { color: var(--white); font-weight: 600; font-size: 11.5px; line-height: 15.5px; }
  .back .section__body { font-weight: 400; font-size: 12.2px; line-height: 16.5px; text-align: justify; }
  .back .section__head { font-size: 17px; }

  .photo { position: absolute; }
  .photo--round { border-radius: 50%; border: 4px solid var(--white); }

  .contact__phone { color: var(--white); font-weight: 800; font-size: 31px; letter-spacing: 0.5px; line-height: 1; white-space: nowrap; }
  .contact__line { color: var(--white); font-weight: 600; font-size: 13.5px; line-height: 1; white-space: nowrap; }

  .fineprint { color: var(--text); font-size: 6.4px; line-height: 8.5px; }
</style>
</head>
<body>

<!-- Front page -->
<section class="flyer flyer--front">
  <svg class="flyer__bg" viewBox="0 0 551 784" width="551" height="784">
    <rect width="551" height="784" fill="#ffffff"/>
    <polygon points="0,0 52,0 551,212 551,246 0,22" fill="#2a9bd8"/>
    <polygon points="0,22 551,246 551,784 0,784" fill="#1b1f24"/>
    <polygon points="0,572 551,800 0,800" fill="#2a9bd8"/>
  </svg>

  <div class="photo" style="left:300px;top:238px;width:251px;height:546px;background:linear-gradient(160deg,#3b3f44 0%,#6b5446 30%,#23262a 60%,#3a2428 80%,#1e2125 100%);opacity:.92;" role="img" aria-label="Athlet im ärmellosen Shirt mit roten Boxhandschuhen"></div>

  <div class="abs brand-name brand-name--dark" style="left:330px;top:84px;width:210px;">VELLMAR</div>

  <div class="abs title-kicker">VELLMAR</div>
  <div class="abs title-main">Nachwuchsförderung<br>und -mangement</div>
  <div class="abs tagline">Wir begleiten dich auf deinem Weg zum Profi</div>

  <div class="abs section" style="left:16px;top:282px;width:330px;">
    <div class="section__head">Karriereplanung</div>
    <p class="section__body" style="margin-top:5px;">Wir haben deine Karriere im Blick! In enger Absprache mit deinen Eltern und dir leiten wir die richtigen Maßnahmen und Schritte ein, um dein Ziel „Profifußballer“ zu realisieren.</p>
  </div>
  <div class="abs section" style="left:16px;top:384px;width:368px;">
    <div class="section__head">Ständiger Ansprechpartner</div>
    <p class="section__body" style="margin-top:5px;">Egal um welchen Themen es sich handelt, wir sind für dich da! Ein vertrauensvolles und freundschaftliches Verhältnis ist uns besonders wichtig.</p>
  </div>
  <div class="abs section" style="left:16px;top:471px;width:262px;">
    <div class="section__head">Rechtsberatung/Vertragsrecht</div>
    <p class="section__body" style="margin-top:5px;">Juristendeutsch und Kleingedrucktes? Kein Problem! Wir helfen dir den Durchblick zu behalten und holen immer das Beste für dich raus.</p>
  </div>

  <div class="photo photo--round" style="left:42px;top:560px;width:124px;height:124px;background:linear-gradient(180deg,#7fae4a,#dfe6ee 55%,#5f8f3a);" role="img" aria-label="Jugendspieler auf der Bank, von hinten"></div>
  <div class="photo photo--round" style="left:165px;top:605px;width:100px;height:100px;background:linear-gradient(150deg,#f2a36a,#f6d6bd 55%,#e28646);" role="img" aria-label="Kind mit Tennisschläger"></div>

  <svg class="abs" style="left:16px;top:716px;" width="32" height="32" viewBox="0 0 24 24"><path fill="#fff" d="M6.6 10.8c1.4 2.8 3.8 5.1 6.6 6.6l2.2-2.2c.3-.3.7-.4 1-.2 1.1.4 2.3.6 3.6.6.6 0 1 .4 1 1V20c0 .6-.4 1-1 1C10.6 21 3 13.4 3 4c0-.6.4-1 1-1h3.5c.6 0 1 .4 1 1 0 1.3.2 2.5.6 3.6.1.3 0 .7-.2 1z"/></svg>
  <div class="abs contact__phone" style="left:64px;top:720px;">07000/1234567</div>
  <svg class="abs" style="left:15px;top:757px;" width="19" height="14" viewBox="0 0 19 14"><rect width="19" height="14" rx="1.5" fill="#fff"/><polyline points="1,1.5 9.5,8 18,1.5" fill="none" stroke="#2a9bd8" stroke-width="1.6"/></svg>
  <div class="abs contact__line" style="left:42px;top:758px;">info@vellmar-sport.de</div>
  <svg class="abs" style="left:200px;top:755px;" width="18" height="18" viewBox="0 0 18 18" fill="none" stroke="#fff" stroke-width="1.6"><circle cx="9" cy="9" r="7.6"/><ellipse cx="9" cy="9" rx="3.4" ry="7.6"/><line x1="1.4" y1="9" x2="16.6" y2="9"/></svg>
  <div class="abs contact__line" style="left:226px;top:758px;">www.vellmar-sport.de</div>
</section>

<!-- Back page -->
<section class="flyer flyer--back back">
  <svg class="flyer__bg" viewBox="0 0 551 784" width="551" height="784">
    <rect width="551" height="784" fill="#ffffff"/>
    <defs>
      <linearGradient id="turf" x1="0" y1="0" x2="1" y2="1">
        <stop offset="0" stop-color="#b8e04c"/>
        <stop offset="0.5" stop-color="#8fcc34"/>
        <stop offset="1" stop-color="#d9f06e"/>
      </linearGradient>
    </defs>
    <polygon points="0,0 551,0 551,150 0,215" fill="url(#turf)" role="img" aria-label="Schachfiguren aus Rasen vor hellgrünem Hintergrund"/>
    <polygon points="0,290 551,64 551,82 0,308" fill="#2a9bd8"/>
    <polygon points="0,308 551,82 551,784 0,784" fill="#1b1f24"/>
    <polygon points="0,582 551,800 0,800" fill="#2a9bd8"/>
  </svg>

  <div class="abs brand-name brand-name--light" style="left:330px;top:250px;width:200px;">VELLMAR</div>

  <svg class="abs" style="left:12px;top:322px;" width="18" height="16" viewBox="0 0 18 16"><circle cx="5" cy="11" r="4.5" fill="#2a9bd8"/><rect x="11" y="1" width="3.5" height="14" rx="1.7" fill="#2a9bd8"/></svg>
  <div class="abs section" style="left:38px;top:318px;width:498px;">
    <div class="section__head">Ausrüstung</div>
    <p class="section__body" style="margin-top:1px;">Wir besorgen dir deine Ausrüstung! Unsere Beziehungen zu den großen Sportartikelherstellern ermöglichen den Abschluss von Ausrüsterverträgen*.</p>
  </div>

  <svg class="abs" style="left:12px;top:388px;" width="18" height="18" viewBox="0 0 18 18" fill="none" stroke="#2a9bd8" stroke-width="1.5"><circle cx="7" cy="5" r="3.5"/><path d="M1 16c0-3.5 2.7-6 6-6s6 2.5 6 6z"/><path d="M13 9l1.5 1.5L17 7"/></svg>
  <div class="abs section" style="left:38px;top:384px;width:498px;">
    <div class="section__head">Vorsorge</div>
    <p class="section__body" style="margin-top:1px;text-align:left;">Verletzungen gehören leider zum Fußball dazu.<br>Wir sichern dich ab, indem wir eine private Zusatzkrankenversicherung für dich abschließen.</p>
  </div>

  <svg class="abs" style="left:10px;top:462px;" width="20" height="20" viewBox="0 0 20 20" fill="none" stroke="#2a9bd8" stroke-width="1.6"><circle cx="4" cy="16" r="2" fill="#2a9bd8"/><path d="M3 9a8 8 0 0 1 8 8"/><path d="M3 4a13 13 0 0 1 13 13"/></svg>
  <div class="abs section" style="left:38px;top:451px;width:498px;">
    <div class="section__head">Kooperationspartner/Netzwerk</div>
    <p class="section__body" style="margin-top:1px;">Ob Entscheidungsträger oder Experte, wir kennen die richtigen Leute. Zusätzlich bieten wir dir eine große Bandbreite an Leistungen, die du jederzeit in Anspruch nehmen kannst**.</p>
  </div>

  <p class="abs fineprint" style="left:12px;top:522px;width:530px;">*Die Entscheidung über einen Ausrüstervertrag liegt beim jeweiligen Hersteller. Ist ein Abschluss nicht möglich, erhältst du zweimal pro Saison neue Fußballschuhe und weitere Ausrüstung.</p>
  <p class="abs fineprint" style="left:12px;top:549px;width:530px;">**Personal Training, Athletik-Training, Ernährungsberatung, Sportpsychologische Betreuung, uvm.</p>

  <div class="photo" style="left:388px;top:545px;width:140px;height:225px;border-radius:40% 40% 30% 30%;background:radial-gradient(circle at 50% 35%,#c04ad0 0%,#3b7ad8 35%,#2fc0c8 55%,rgba(27,31,36,0) 75%);" role="img" aria-label="Farbenfrohe Illustration eines Fußballspielers mit Ball und Pokal"></div>

  <div class="photo photo--round" style="left:22px;top:572px;width:122px;height:122px;background:linear-gradient(160deg,#b9b2a8,#6d6a66 50%,#d9d6d0);" role="img" aria-label="Sprinter in Startposition auf der Laufbahn"></div>
  <div class="photo photo--round" style="left:160px;top:590px;width:108px;height:108px;background:radial-gradient(circle at 55% 55%,#c8342c 0%,#3a2c4c 45%,#15162a 100%);" role="img" aria-label="Basketballspieler im Scheinwerferlicht"></div>
  <div class="photo photo--round" style="left:283px;top:614px;width:84px;height:84px;background:linear-gradient(160deg,#a8b0b6,#c23a35 55%,#3b3e44);" role="img" aria-label="Radrennfahrer mit Helm"></div>

  <svg class="abs" style="left:10px;top:710px;" width="32" height="32" viewBox="0 0 24 24"><path fill="#fff" d="M6.6 10.8c1.4 2.8 3.8 5.1 6.6 6.6l2.2-2.2c.3-.3.7-.4 1-.2 1.1.4 2.3.6 3.6.6.6 0 1 .4 1 1V20c0 .6-.4 1-1 1C10.6 21 3 13.4 3 4c0-.6.4-1 1-1h3.5c.6 0 1 .4 1 1 0 1.3.2 2.5.6 3.6.1.3 0 .7-.2 1z"/></svg>
  <div class="abs contact__phone" style="left:62px;top:714px;">07000/1234567</div>
  <svg class="abs" style="left:10px;top:755px;" width="19" height="14" viewBox="0 0 19 14"><rect width="19" height="14" rx="1.5" fill="#fff"/><polyline points="1,1.5 9.5,8 18,1.5" fill="none" stroke="#2a9bd8" stroke-width="1.6"/></svg>
  <div class="abs contact__line" style="left:38px;top:756px;">info@vellmar-sport.de</div>
  <svg class="abs" style="left:198px;top:753px;" width="18" height="18" viewBox="0 0 18 18" fill="none" stroke="#fff" stroke-width="1.6"><circle cx="9" cy="9" r="7.6"/><ellipse cx="9" cy="9" rx="3.4" ry="7.6"/><line x1="1.4" y1="9" x2="16.6" y2="9"/></svg>
  <div class="abs contact__line" style="left:224px;top:756px;">www.vellmar-sport.de</div>
</section>

</body>
</html>
```